Business Card & Stationary Design Project

We are looking for some creative direction for business cards and our stationary.

We are a global logistics firm that has recently changed its name to Marrick Global Logistics and we have a new website due out tomorrow (www.marrick.com.au).

The colours of the company are rich navy tones, I would like to have business cards that fit together to make one picture on the back (possibly an old map of the world??), and the front to be modern contemporary looking.

But I am open to suggestions, so just incorporate our new logo and get going!
Updates

Hi Everyone,

Thank you for all of your designs so far and the time you have put into it.

I have asked many of you for amendments to see if we can get a final product, so with this in mind I am extending the deadline by a few days.

Good luck and thank you once again.

Please message me direct if you need any clarification.

Kind Regards
Colin

Reason: As outlined the extra 3 days is for amendments and changes to the current submissions. Thanks Colin

Industry/Entity Type

Business

```html
<!DOCTYPE html>
<html lang="en">
<head>
<meta charset="utf-8">
<title>Marrick Global Logistics – Business Cards</title>
<link rel="stylesheet" href="https://fonts.googleapis.com/css2?family=Cinzel:wght@400&family=Exo+2:wght@300&display=swap">
<style>
  :root {
    --page-bg: #eeeef2;
    --navy-light: #1f4f8e;
    --navy-deep: #0f2f63;
    --contact-blue: #56b6f0;
    --icon-white: #ffffff;
    --mark-white: #ffffff;
    --mark-navy: #1b2a66;
    --parchment-light: #eee8d8;
    --parchment: #e2d8c0;
    --parchment-dark: #cbbd9c;
    --globe-light: #6fb0e8;
    --globe-deep: #1a58a8;
    --card-shadow: rgba(20, 30, 60, 0.22);
  }
  * { box-sizing: border-box; margin: 0; padding: 0; }
  html, body { width: 1200px; height: 900px; overflow: hidden; }
  body {
    background: var(--page-bg);
    position: relative;
    font-family: "Exo 2", sans-serif;
  }
  .card {
    position: absolute;
    top: 300px;
    width: 525px;
    height: 300px;
    border-radius: 22px;
    overflow: hidden;
    box-shadow: 0 14px 30px var(--card-shadow);
  }
  .card-front {
    left: 50px;
    background: linear-gradient(160deg, var(--navy-light) 0%, var(--navy-deep) 100%);
  }
  .card-back {
    left: 625px;
    background: var(--parchment);
  }
  .wordmark {
    position: absolute;
    font-family: "Cinzel", serif;
    font-weight: 400;
    font-size: 19px;
    letter-spacing: 0.3em;
    white-space: nowrap;
  }
  .card-front .wordmark { left: 34px; top: 26px; color: var(--mark-white); }
  .card-back .wordmark { left: 40px; top: 58px; color: var(--mark-navy); }

  .contact-list {
    position: absolute;
    left: 30px;
    top: 80px;
    list-style: none;
    color: var(--contact-blue);
    font-weight: 300;
    font-size: 15.5px;
    line-height: 19px;
  }
  .contact-list li { display: flex; align-items: flex-start; gap: 8px; }
  .contact-list .indent { padding-left: 24px; }
  .contact-icon { width: 16px; height: 16px; flex: none; margin-top: 1px; }

  .globe-area-large {
    position: absolute;
    left: 270px;
    top: 110px;
    width: 340px;
    height: 340px;
    border-radius: 50%;
    background: linear-gradient(150deg, var(--globe-light) 0%, var(--globe-deep) 100%);
  }
  .map-area {
    position: absolute;
    inset: 0;
    background: linear-gradient(120deg, var(--parchment-light) 0%, var(--parchment) 45%, var(--parchment-dark) 100%);
  }
  .globe-area-small {
    position: absolute;
    left: 365px;
    top: 120px;
    width: 118px;
    height: 98px;
    border-radius: 50%;
    background: linear-gradient(150deg, var(--globe-light) 0%, var(--globe-deep) 100%);
  }
</style>
</head>
<body>

<section class="card card-front" aria-label="Business card front">
  <div class="globe-area-large" role="img" aria-label="Glossy blue globe showing Asia and Australia"></div>
  <p class="wordmark">MARRICK GLOBAL LOGISTICS</p>
  <ul class="contact-list">
    <li>
      <svg class="contact-icon" viewBox="0 0 16 16" aria-hidden="true"><path d="M2 8 8 2.5 14 8M4 7v7h8V7" fill="none" stroke="var(--icon-white)" stroke-width="1.6"/></svg>
      <span>58 Harbour Lane Street</span>
    </li>
    <li class="indent"><span>Pyrmont Point NSW 2009</span></li>
    <li>
      <svg class="contact-icon" viewBox="0 0 16 16" aria-hidden="true"><path d="M3 3h3l1 3-2 1a8 8 0 0 0 4 4l1-2 3 1v3c-6 0-10-4-10-10z" fill="var(--icon-white)"/></svg>
      <span>02 9174 2250</span>
    </li>
    <li>
      <svg class="contact-icon" viewBox="0 0 16 16" aria-hidden="true"><rect x="4.5" y="1.5" width="7" height="13" rx="1.2" fill="none" stroke="var(--icon-white)" stroke-width="1.5"/><circle cx="8" cy="12" r="0.9" fill="var(--icon-white)"/></svg>
      <span>0400718362</span>
    </li>
    <li>
      <svg class="contact-icon" viewBox="0 0 16 16" aria-hidden="true"><rect x="2" y="6" width="12" height="7" rx="1" fill="var(--icon-white)"/><rect x="4.5" y="2" width="7" height="4" fill="none" stroke="var(--icon-white)" stroke-width="1.3"/></svg>
      <span>029261 4830</span>
    </li>
    <li>
      <svg class="contact-icon" viewBox="0 0 16 16" aria-hidden="true"><rect x="1.5" y="3.5" width="13" height="9" fill="none" stroke="var(--icon-white)" stroke-width="1.4"/><path d="M1.5 3.5 8 9l6.5-5.5" fill="none" stroke="var(--icon-white)" stroke-width="1.4"/></svg>
      <span>colin@marrick.com.au</span>
    </li>
    <li>
      <svg class="contact-icon" viewBox="0 0 16 16" aria-hidden="true"><circle cx="8" cy="8" r="6.3" fill="none" stroke="var(--icon-white)" stroke-width="1.3"/><path d="M1.7 8h12.6M8 1.7c-3 3.5-3 9 0 12.6M8 1.7c3 3.5 3 9 0 12.6" fill="none" stroke="var(--icon-white)" stroke-width="1.1"/></svg>
      <span>marrick.com.au</span>
    </li>
  </ul>
</section>

<section class="card card-back" aria-label="Business card back">
  <div class="map-area" role="img" aria-label="Faded antique map of the world in parchment tones"></div>
  <p class="wordmark">MARRICK GLOBAL LOGISTICS</p>
  <div class="globe-area-small" role="img" aria-label="Small glossy blue globe"></div>
</section>

</body>
</html>
```